Ferro Lanes - explore habits of productive people

Ferro Lanes is a social place around habits and productivity

The full brief below:

https://files.quorvanta.com/sheet/d/7Kp-RwTZMX2uqEebH-Y-cNdt4TgsWmFkyQoPJhwbrzVe/view?mode=viewer

Colors

Designer to choose colors to be used in the design.

Requirements
Must have
• - a feed page to display habits
• - a habit page to add a habit
• / clean, no cluttered design, lots of white space
• / inspired by material design or other design system
Nice to have
• - user page

```html
<!DOCTYPE html>
<html lang="en">
<head>
<meta charset="utf-8">
<title>Ferro Lanes – Feed</title>
<link href="https://fonts.googleapis.com/css2?family=Source+Sans+3:wght@300;400;600;700&display=swap" rel="stylesheet">
<style>
:root{
  --blue:#1a8fd6;
  --blue-light:#2aa9e6;
  --green:#3aa51c;
  --dark:#262b30;
  --darker:#1c2024;
  --ink:#2b2b2b;
  --muted:#6d6d6d;
  --line:#e3e3e3;
  --topbar:#e9e9e9;
  --page:#ffffff;
}
*{box-sizing:border-box;margin:0;padding:0}
html,body{width:1200px;height:1200px;overflow:hidden;background:#f4f4f4}
body{font-family:"Source Sans 3",sans-serif;color:var(--ink)}
.page{position:absolute;left:288px;top:0;width:780px;height:1500px;background:var(--page);transform:scale(.8);transform-origin:0 0;overflow:hidden}
.abs{position:absolute}
.topbar{left:0;top:0;width:780px;height:16px;background:var(--topbar)}
.topnav{display:flex;gap:17px;left:97px;top:5px;font-size:5.5px;color:#333;letter-spacing:.2px}
.mailbtn{left:569px;top:0;width:113px;height:16px;background:var(--blue);color:#fff;font-size:6px;display:flex;align-items:center;justify-content:center;gap:3px}
.header{left:0;top:16px;width:780px;height:27px;background:var(--dark)}
.brand{font-weight:700;color:#fff;font-size:15px}
.search{left:367px;top:22px;width:201px;height:15px;background:#353c43;border-radius:2px;color:#7d858d;font-size:5.5px;padding:4px 8px}
.hero{left:0;top:43px;width:780px;height:272px;background:linear-gradient(90deg,#e7e5e0 0%,#d9d5cc 25%,#b9a58a 35%,#f3f1ea 50%,#f2e7b8 75%,#d7b34c 100%)}
.hero-box{left:398px;top:100px;width:284px;height:158px;background:rgba(46,46,46,.78);padding:27px 11px}
.hero-box p{font-size:12.5px;color:#fff;line-height:19px}
.hero-box .accent{color:var(--blue-light)}
.hero-box .sub{font-weight:300;font-size:14px;margin-top:6px}
.btn-hero{margin-top:10px;display:inline-block;background:var(--blue);color:#fff;font-size:8px;border-radius:10px;padding:5px 17px}
.strip{left:0;top:315px;width:780px;height:32px;border:1px solid var(--line);border-top:0}
.strip-text{left:97px;top:326px;font-size:6.5px;color:#333}
.btn-sm{height:17px;color:#fff;font-size:6px;display:flex;align-items:center;justify-content:center;gap:5px}
.side-h{font-size:8px;font-weight:700}
.side-p{font-size:6.5px;color:#555;line-height:13.5px}
.outline-green{border:1px solid var(--green);color:var(--green);font-size:6.5px;display:flex;align-items:center;justify-content:center}
.popular-bar{left:98px;top:462px;width:150px;height:22px;background:var(--blue);color:#fff;font-size:8px;font-weight:700;padding:6px 7px}
.avatar{width:52px;height:52px;border-radius:50%;background:linear-gradient(135deg,#7d6a5c,#3c3a3f)}
.badge{width:16px;height:16px;border-radius:50%;background:#222;color:#fff;font-size:7px;font-weight:700;display:flex;align-items:center;justify-content:center;border:1.5px solid #fff}
.pop-title{font-size:7px;line-height:12px;color:#222;width:80px}
.meta{display:flex;align-items:center;gap:4px;font-size:5.5px;color:#666}
.tag{height:17px;border:1px solid #ddd;border-radius:9px;font-size:6px;color:#888;display:flex;align-items:center;justify-content:center}
.card{left:262px;width:421px;height:127px;background:#fff;box-shadow:0 1px 4px rgba(0,0,0,.18)}
.card-img{position:absolute;left:0;top:0;width:133px;height:127px}
.card-body{position:absolute;left:148px;top:15px;width:260px}
.card-title{font-size:10px;color:#222}
.card-by{font-size:6px;color:#555;margin-top:5px}
.card-by b{color:var(--green);font-weight:600}
.card-by i{color:var(--blue);font-style:normal;font-weight:600}
.card-text{font-size:6.8px;color:#666;line-height:13.6px;margin-top:6px}
.card .meta{margin-top:11px;gap:5px}
.pager{left:262px;top:1264px;display:flex;font-size:7px}
.pager span{height:17px;padding:0 5.5px;border:1px solid #e4e4e4;margin-right:-1px;display:flex;align-items:center;color:var(--blue)}
.pager .off{color:#888}
.pager .on{background:var(--green);color:#fff;border-color:var(--green)}
.footer{left:0;top:1324px;width:780px;height:146px;background:#22272b}
.footbar{left:0;top:1470px;width:780px;height:30px;background:var(--darker);color:#ddd;font-size:6px;display:flex;align-items:center;justify-content:center}
.foot-h{font-size:11px;font-weight:700;color:#fff}
.foot-link{font-size:6.5px;color:#e6e6e6}
.social{width:20px;height:20px}
</style>
</head>
<body>
<div class="page">
  <div class="abs topbar"></div>
  <nav class="abs topnav"><span>ABOUT</span><span>ARTICLES</span><span>BOOKS</span><span>FAVOURITES</span><span>FREE NEWSLETTER</span></nav>
  <div class="abs mailbtn">
    <svg width="7" height="5" viewBox="0 0 7 5"><rect x=".4" y=".4" width="6.2" height="4.2" fill="none" stroke="#fff" stroke-width=".7"/><path d="M.4 .4 3.5 3 6.6 .4" fill="none" stroke="#fff" stroke-width=".7"/></svg>
    MAIL US:info@ferrolanes.com
  </div>

  <header class="abs header"></header>
  <div class="abs brand" style="left:97px;top:19px">Ferro Lanes</div>
  <div class="abs search">Search The Community
    <svg class="abs" style="right:5px;top:4px" width="7" height="7" viewBox="0 0 7 7"><circle cx="3" cy="3" r="2.2" fill="none" stroke="#8a929a" stroke-width=".8"/><path d="M4.6 4.6 6.6 6.6" stroke="#8a929a" stroke-width=".8"/></svg>
  </div>
  <svg class="abs" style="left:597px;top:26px" width="10" height="7" viewBox="0 0 10 7"><path d="M0 .5h10M0 3.5h10M0 6.5h10" stroke="#fff" stroke-width="1"/></svg>
  <div class="abs" style="left:627px;top:21px;width:18px;height:18px;border-radius:50%;background:#fff;overflow:hidden">
    <svg width="18" height="18" viewBox="0 0 18 18"><circle cx="9" cy="7" r="3.5" fill="#9aa0a6"/><path d="M2 18c1-5 4-6 7-6s6 1 7 6z" fill="#9aa0a6"/></svg>
  </div>
  <div class="abs" style="left:652px;top:25px;color:#fff;font-size:6.5px;font-weight:600">Log In</div>
  <svg class="abs" style="left:677px;top:27px" width="6" height="4" viewBox="0 0 6 4"><path d="M.5.5 3 3 5.5.5" fill="none" stroke="#ccc" stroke-width=".8"/></svg>

  <section class="abs hero" role="img" aria-label="Photo of a young woman sitting by a sunlit window holding a cup of coffee, with flowers in the foreground"></section>
  <div class="abs hero-box">
    <p>Professionals are the architects of their habits.</p>
    <p class="accent">Amateurs are the victims of their habits.</p>
    <p class="sub">You’ve come to the right place!</p>
    <span class="btn-hero">Get Started</span>
  </div>

  <div class="abs strip"></div>
  <div class="abs strip-text">Curious about habits? Looking to connect on social technology? You’ve come to the right place!</div>
  <div class="abs btn-sm" style="left:536px;top:322px;width:88px;background:var(--blue)">
    <svg width="8" height="8" viewBox="0 0 8 8"><rect x=".5" y=".5" width="6" height="7" fill="none" stroke="#fff" stroke-width=".8"/><path d="M2 3h3M2 5h2" stroke="#fff" stroke-width=".8"/></svg>Create New Post</div>
  <div class="abs btn-sm" style="left:633px;top:322px;width:49px;background:var(--green)">
    <svg width="10" height="6" viewBox="0 0 10 6"><path d="M0 .5h10M0 3h7M0 5.5h4" stroke="#fff" stroke-width=".9"/></svg>&nbsp;Filter</div>

  <!-- Sidebar -->
  <div class="abs side-h" style="left:98px;top:371px">WELCOME, VISITOR!</div>
  <p class="abs side-p" style="left:98px;top:388px;width:152px">It looks like you’re new here. If you want to get involved, Sign In now, and stay updated!</p>
  <div class="abs outline-green" style="left:98px;top:425px;width:43px;height:17px">Sign In</div>
  <div class="abs popular-bar">MOST POPULAR</div>

  <div class="abs avatar" style="left:101px;top:508px" role="img" aria-label="Profile photo of a bearded man"></div>
  <div class="abs badge" style="left:99px;top:505px">1.</div>
  <div class="abs pop-title" style="left:162px;top:517px">Praesent blandit turpis egestas vitae congue</div>
  <div class="abs meta" style="left:163px;top:547px"><svg width="9" height="8" viewBox="0 0 9 8"><path d="M.5 3.5h2v4h-2zM2.5 3.5 4.5.5c1 0 1 1 .7 2H8c.5 0 .7.5.5 1L7.6 7.5H2.5" fill="none" stroke="var(--blue)" stroke-width=".8"/></svg>12<span style="width:10px"></span><svg width="11" height="8" viewBox="0 0 11 8"><ellipse cx="5.5" cy="3.5" rx="5" ry="3" fill="none" stroke="var(--green)" stroke-width=".9"/><path d="M2 6 1 7.7 4 6.4" fill="none" stroke="var(--green)" stroke-width=".9"/></svg>09</div>

  <div class="abs avatar" style="left:101px;top:585px;background:linear-gradient(135deg,#c77a4e,#5a3a2c)" role="img" aria-label="Profile photo of a woman with curly hair"></div>
  <div class="abs badge" style="left:99px;top:582px">2.</div>
  <div class="abs pop-title" style="left:162px;top:595px">Praesent blandit turpis egestas vitae congue</div>
  <div class="abs meta" style="left:163px;top:625px"><svg width="9" height="8" viewBox="0 0 9 8"><path d="M.5 3.5h2v4h-2zM2.5 3.5 4.5.5c1 0 1 1 .7 2H8c.5 0 .7.5.5 1L7.6 7.5H2.5" fill="none" stroke="var(--blue)" stroke-width=".8"/></svg>12<span style="width:10px"></span><svg width="11" height="8" viewBox="0 0 11 8"><ellipse cx="5.5" cy="3.5" rx="5" ry="3" fill="none" stroke="var(--green)" stroke-width=".9"/><path d="M2 6 1 7.7 4 6.4" fill="none" stroke="var(--green)" stroke-width=".9"/></svg>09</div>

  <div class="abs avatar" style="left:101px;top:663px;background:linear-gradient(135deg,#d9a878,#2e5c8a)" role="img" aria-label="Profile photo of a smiling woman"></div>
  <div class="abs badge" style="left:99px;top:660px">3.</div>
  <div class="abs pop-title" style="left:162px;top:672px">Praesent blandit turpis egestas vitae congue</div>
  <div class="abs meta" style="left:163px;top:702px"><svg width="9" height="8" viewBox="0 0 9 8"><path d="M.5 3.5h2v4h-2zM2.5 3.5 4.5.5c1 0 1 1 .7 2H8c.5 0 .7.5.5 1L7.6 7.5H2.5" fill="none" stroke="var(--blue)" stroke-width=".8"/></svg>12<span style="width:10px"></span><svg width="11" height="8" viewBox="0 0 11 8"><ellipse cx="5.5" cy="3.5" rx="5" ry="3" fill="none" stroke="var(--green)" stroke-width=".9"/><path d="M2 6 1 7.7 4 6.4" fill="none" stroke="var(--green)" stroke-width=".9"/></svg>09</div>

  <div class="abs avatar" style="left:101px;top:740px;background:linear-gradient(135deg,#5f7b5a,#2b2622)" role="img" aria-label="Profile photo of a man with a beard"></div>
  <div class="abs badge" style="left:99px;top:737px">4.</div>
  <div class="abs pop-title" style="left:162px;top:750px">Praesent blandit turpis egestas vitae congue</div>
  <div class="abs meta" style="left:163px;top:780px"><svg width="9" height="8" viewBox="0 0 9 8"><path d="M.5 3.5h2v4h-2zM2.5 3.5 4.5.5c1 0 1 1 .7 2H8c.5 0 .7.5.5 1L7.6 7.5H2.5" fill="none" stroke="var(--blue)" stroke-width=".8"/></svg>12<span style="width:10px"></span><svg width="11" height="8" viewBox="0 0 11 8"><ellipse cx="5.5" cy="3.5" rx="5" ry="3" fill="none" stroke="var(--green)" stroke-width=".9"/><path d="M2 6 1 7.7 4 6.4" fill="none" stroke="var(--green)" stroke-width=".9"/></svg>09</div>

  <div class="abs side-h" style="left:98px;top:819px">POPULAR TAGS</div>
  <div class="abs tag" style="left:98px;top:841px;width:44px">Commodo</div>
  <div class="abs tag" style="left:150px;top:841px;width:45px">Commodo</div>
  <div class="abs tag" style="left:202px;top:841px;width:45px">Commodo</div>
  <div class="abs tag" style="left:98px;top:872px;width:28px">Sed</div>
  <div class="abs tag" style="left:138px;top:872px;width:44px">faucibus</div>
  <div class="abs tag" style="left:192px;top:872px;width:45px">Commodo</div>
  <div class="abs tag" style="left:98px;top:900px;width:44px">Commodo</div>
  <div class="abs tag" style="left:150px;top:900px;width:45px">Commodo</div>
  <div class="abs tag" style="left:202px;top:900px;width:45px">Commodo</div>
  <div class="abs tag" style="left:98px;top:931px;width:28px">Sed</div>
  <div class="abs tag" style="left:138px;top:931px;width:44px">faucibus</div>
  <div class="abs tag" style="left:192px;top:931px;width:45px">Commodo</div>

  <!-- Feed -->
  <article class="abs card" style="top:372px">
    <div class="card-img" role="img" aria-label="Coffee mug beside a note about creating habits" style="background:linear-gradient(135deg,#6b3a22,#b9a685 45%,#e8e1cf 70%,#3b6f9a)"></div>
    <div class="card-body"><h3 class="card-title" style="font-weight:400">Mauris nec imperdiet massa, at elementum nibh</h3>
      <p class="card-by">By <b>Tobin</b> on <i>Good</i></p>
      <p class="card-text">Vivamus orci lorem, semper ut porta ut, egestas vitae justo. Vivamus male-suada vestibulum ultricies. Sed nec mattis magna. Etiam facilisis eget dolor eget elementum. Ut posuere tortor nisl, eget commodo ante eleifend id....</p>
      <div class="meta"><svg width="10" height="9" viewBox="0 0 9 8"><path d="M.5 3.5h2v4h-2zM2.5 3.5 4.5.5c1 0 1 1 .7 2H8c.5 0 .7.5.5 1L7.6 7.5H2.5" fill="none" stroke="#777" stroke-width=".7"/></svg>12<span style="width:6px"></span><svg width="11" height="9" viewBox="0 0 11 8"><ellipse cx="5.5" cy="3.5" rx="5" ry="3" fill="none" stroke="#777" stroke-width=".8"/><path d="M2 6 1 7.7 4 6.4" fill="none" stroke="#777" stroke-width=".8"/></svg>09</div></div>
  </article>
  <article class="abs card" style="top:518px">
    <div class="card-img" role="img" aria-label="Feet on asphalt between arrows marked old habits and change" style="background:linear-gradient(135deg,#3d3d3d,#7a7a78 50%,#4a4a48)"></div>
    <div class="card-body"><h3 class="card-title" style="font-weight:400">Mauris nec imperdiet massa, at elementum nibh</h3>
      <p class="card-by">By <b>Tobin</b> on <i>Good</i></p>
      <p class="card-text">Vivamus orci lorem, semper ut porta ut, egestas vitae justo. Vivamus male-suada vestibulum ultricies. Sed nec mattis magna. Etiam facilisis eget dolor eget elementum. Ut posuere tortor nisl, eget commodo ante eleifend id....</p>
      <div class="meta"><svg width="10" height="9" viewBox="0 0 9 8"><path d="M.5 3.5h2v4h-2zM2.5 3.5 4.5.5c1 0 1 1 .7 2H8c.5 0 .7.5.5 1L7.6 7.5H2.5" fill="none" stroke="#777" stroke-width=".7"/></svg>12<span style="width:6px"></span><svg width="11" height="9" viewBox="0 0 11 8"><ellipse cx="5.5" cy="3.5" rx="5" ry="3" fill="none" stroke="#777" stroke-width=".8"/><path d="M2 6 1 7.7 4 6.4" fill="none" stroke="#777" stroke-width=".8"/></svg>09</div></div>
  </article>
  <article class="abs card" style="top:664px">
    <div class="card-img" role="img" aria-label="Wrench gripping a tag labelled bad habits on dark wood" style="background:linear-gradient(135deg,#1e1e1e,#3a3835 55%,#242220)"></div>
    <div class="card-body"><h3 class="card-title" style="font-weight:400">Mauris nec imperdiet massa, at elementum nibh</h3>
      <p class="card-by">By <b>Tobin</b> on <i>Bad</i></p>
      <p class="card-text">Vivamus orci lorem, semper ut porta ut, egestas vitae justo. Vivamus male-suada vestibulum ultricies. Sed nec mattis magna. Etiam facilisis eget dolor eget elementum. Ut posuere tortor nisl, eget commodo ante eleifend id....</p>
      <div class="meta"><svg width="10" height="9" viewBox="0 0 9 8"><path d="M.5 3.5h2v4h-2zM2.5 3.5 4.5.5c1 0 1 1 .7 2H8c.5 0 .7.5.5 1L7.6 7.5H2.5" fill="none" stroke="#777" stroke-width=".7"/></svg>12<span style="width:6px"></span><svg width="11" height="9" viewBox="0 0 11 8"><ellipse cx="5.5" cy="3.5" rx="5" ry="3" fill="none" stroke="#777" stroke-width=".8"/><path d="M2 6 1 7.7 4 6.4" fill="none" stroke="#777" stroke-width=".8"/></svg>09</div></div>
  </article>
  <article class="abs card" style="top:810px">
    <div class="card-img" role="img" aria-label="Woman sitting on the floor with a laptop against a white brick wall" style="background:linear-gradient(135deg,#ecebe8,#d6d4cf 50%,#5c6a80 80%,#e9e8e5)"></div>
    <div class="card-body"><h3 class="card-title" style="font-weight:400">Mauris nec imperdiet massa, at elementum nibh</h3>
      <p class="card-by">By <b>Tobin</b> on <i>Good</i></p>
      <p class="card-text">Vivamus orci lorem, semper ut porta ut, egestas vitae justo. Vivamus male-suada vestibulum ultricies. Sed nec mattis magna. Etiam facilisis eget dolor eget elementum. Ut posuere tortor nisl, eget commodo ante eleifend id....</p>
      <div class="meta"><svg width="10" height="9" viewBox="0 0 9 8"><path d="M.5 3.5h2v4h-2zM2.5 3.5 4.5.5c1 0 1 1 .7 2H8c.5 0 .7.5.5 1L7.6 7.5H2.5" fill="none" stroke="#777" stroke-width=".7"/></svg>12<span style="width:6px"></span><svg width="11" height="9" viewBox="0 0 11 8"><ellipse cx="5.5" cy="3.5" rx="5" ry="3" fill="none" stroke="#777" stroke-width=".8"/><path d="M2 6 1 7.7 4 6.4" fill="none" stroke="#777" stroke-width=".8"/></svg>09</div></div>
  </article>
  <article class="abs card" style="top:956px">
    <div class="card-img" role="img" aria-label="Smiling man with a phone and a red mug in a kitchen" style="background:linear-gradient(135deg,#6e4a3a,#a08a78 45%,#8f939a 75%,#c73a3a)"></div>
    <div class="card-body"><h3 class="card-title" style="font-weight:400">Mauris nec imperdiet massa, at elementum nibh</h3>
      <p class="card-by">By <b>Tobin</b> on <i>Bad</i></p>
      <p class="card-text">Vivamus orci lorem, semper ut porta ut, egestas vitae justo. Vivamus male-suada vestibulum ultricies. Sed nec mattis magna. Etiam facilisis eget dolor eget elementum. Ut posuere tortor nisl, eget commodo ante eleifend id....</p>
      <div class="meta"><svg width="10" height="9" viewBox="0 0 9 8"><path d="M.5 3.5h2v4h-2zM2.5 3.5 4.5.5c1 0 1 1 .7 2H8c.5 0 .7.5.5 1L7.6 7.5H2.5" fill="none" stroke="#777" stroke-width=".7"/></svg>12<span style="width:6px"></span><svg width="11" height="9" viewBox="0 0 11 8"><ellipse cx="5.5" cy="3.5" rx="5" ry="3" fill="none" stroke="#777" stroke-width=".8"/><path d="M2 6 1 7.7 4 6.4" fill="none" stroke="#777" stroke-width=".8"/></svg>09</div></div>
  </article>
  <article class="abs card" style="top:1102px">
    <div class="card-img" role="img" aria-label="Two children eating breakfast with orange juice at a table" style="background:linear-gradient(135deg,#8a6a50,#d8c0a0 45%,#f0a040 70%,#c9b89c)"></div>
    <div class="card-body"><h3 class="card-title" style="font-weight:400">Mauris nec imperdiet massa, at elementum nibh</h3>
      <p class="card-by">By <b>Tobin</b> on <i>Good</i></p>
      <p class="card-text">Vivamus orci lorem, semper ut porta ut, egestas vitae justo. Vivamus male-suada vestibulum ultricies. Sed nec mattis magna. Etiam facilisis eget dolor eget elementum. Ut posuere tortor nisl, eget commodo ante eleifend id....</p>
      <div class="meta"><svg width="10" height="9" viewBox="0 0 9 8"><path d="M.5 3.5h2v4h-2zM2.5 3.5 4.5.5c1 0 1 1 .7 2H8c.5 0 .7.5.5 1L7.6 7.5H2.5" fill="none" stroke="#777" stroke-width=".7"/></svg>12<span style="width:6px"></span><svg width="11" height="9" viewBox="0 0 11 8"><ellipse cx="5.5" cy="3.5" rx="5" ry="3" fill="none" stroke="#777" stroke-width=".8"/><path d="M2 6 1 7.7 4 6.4" fill="none" stroke="#777" stroke-width=".8"/></svg>09</div></div>
  </article>

  <nav class="abs pager">
    <span class="off">First</span><span class="off">Previous</span><span class="on">1</span><span>2</span><span>3</span><span>4</span><span>5</span><span>6</span><span>7</span><span>8</span><span>9</span><span>10</span><span>Next</span><span>Last</span>
  </nav>

  <footer class="abs footer"></footer>
  <div class="abs brand" style="left:97px;top:1351px">Ferro Lanes</div>
  <div class="abs" style="left:97px;top:1382px;display:flex;align-items:center;gap:6px;color:#eee;font-size:6.5px">
    <svg width="14" height="10" viewBox="0 0 14 10"><rect x=".5" y=".5" width="13" height="9" fill="none" stroke="#ddd" stroke-width=".8"/><path d="M.5 .5 7 6 13.5 .5" fill="none" stroke="#ddd" stroke-width=".8"/></svg>
    Mail Us: info@ferrolanes.com</div>
  <div class="abs social" style="left:97px;top:1409px;background:#3b5a9a"></div>
  <div class="abs social" style="left:119px;top:1409px;background:#e3264a"></div>
  <div class="abs social" style="left:141px;top:1409px;background:#25a3dd"></div>

  <div class="abs foot-h" style="left:272px;top:1349px">Quick Links</div>
  <div class="abs foot-link" style="left:274px;top:1378px">About</div>
  <div class="abs foot-link" style="left:274px;top:1395px">Articles</div>
  <div class="abs foot-link" style="left:274px;top:1411px">Books</div>
  <div class="abs foot-link" style="left:274px;top:1428px">Favourites</div>
  <div class="abs foot-link" style="left:325px;top:1378px">Downloads</div>
  <div class="abs foot-link" style="left:325px;top:1395px">Contact us</div>

  <div class="abs foot-h" style="left:419px;top:1349px">Newsletter Subscribe</div>
  <div class="abs" style="left:419px;top:1376px;width:224px;height:35px;background:#fff;font-size:6.5px;color:#888;padding:13px 13px">Enter Your Mail Id</div>
  <div class="abs" style="left:643px;top:1376px;width:39px;height:35px;background:var(--blue);display:flex;align-items:center;justify-content:center">
    <svg width="18" height="16" viewBox="0 0 18 16"><path d="M1 7 17 1 13 15 8 10z" fill="#fff"/><path d="M8 10 17 1 6 14z" fill="#d5ecf9"/></svg>
  </div>

  <div class="abs footbar">© 2018 Ferro Lanes. All Rights Reserved | Privacy Policy</div>
</div>
</body>
</html>
```